lawn sign

Lawn Sign
Roofing Gutters Windows

Target Market(s)

roofing

Font styles to use
Sans Serif

Colors
86cfc6
33a6d7
fbee3f
faa54b

Requirements
Must have
• my logo
Nice to have
• designer for now

```html
<!DOCTYPE html>
<html lang="en">
<head>
<meta charset="utf-8">
<title>Harbor Ridge Exteriors – Lawn Sign Options</title>
<link href="https://fonts.googleapis.com/css2?family=Cinzel:wght@700&display=swap" rel="stylesheet">
<style>
  :root {
    --page: #eef0ee;
    --sign-white: #ffffff;
    --name-ink: #1b2f5e;
    --mark-tint: #d7ece9;
    --green-dark: #1f9345;
    --green-light: #8cc63f;
    --blue-light: #2a8ccb;
    --blue-dark: #1b2f5e;
    --tagline: #ffffff;
  }
  * { margin: 0; padding: 0; box-sizing: border-box; }
  html, body { width: 838px; height: 1200px; overflow: hidden; }
  body {
    background: var(--page);
    position: relative;
    font-family: "Cinzel", serif;
  }
  .lawn-sign {
    position: absolute;
    left: 192px;
    width: 440px;
    height: 301px;
    background: var(--sign-white);
    box-shadow: 0 4px 14px rgba(0,0,0,0.15);
    overflow: hidden;
  }
  .lawn-sign--green { top: 82px; }
  .lawn-sign--blue { top: 715px; }
  .lawn-sign__art { position: absolute; inset: 0; }
  .brand-dot {
    position: absolute;
    left: 74px;
    top: 40px;
    width: 90px;
    height: 90px;
    border-radius: 50%;
    background: var(--mark-tint);
  }
  .brand-name {
    position: absolute;
    left: 184px;
    top: 60px;
    width: 230px;
    color: var(--name-ink);
    font-weight: 700;
    font-size: 22px;
    line-height: 1.2;
    letter-spacing: 0.3px;
  }
  .tagline {
    position: absolute;
    left: 0;
    right: 0;
    top: 234px;
    text-align: center;
    color: var(--tagline);
    font-weight: 700;
    font-size: 22px;
    letter-spacing: 0.2px;
    white-space: nowrap;
  }
</style>
</head>
<body>

  <section class="lawn-sign lawn-sign--green">
    <svg class="lawn-sign__art" viewBox="0 0 440 301" width="440" height="301" aria-hidden="true">
      <defs>
        <linearGradient id="accent-green" x1="0" x2="1" y1="0" y2="0">
          <stop offset="0" stop-color="#1f9345"/>
          <stop offset="1" stop-color="#8cc63f"/>
        </linearGradient>
        <linearGradient id="band-green" x1="0" x2="1" y1="0" y2="0">
          <stop offset="0" stop-color="#8cc63f"/>
          <stop offset="1" stop-color="#1f9345"/>
        </linearGradient>
      </defs>
      <path d="M0 166 Q220 236 440 164 L440 301 L0 301 Z" fill="url(#accent-green)"/>
      <path d="M0 182 Q220 226 440 176 L440 301 L0 301 Z" fill="url(#band-green)"/>
    </svg>
    <div class="brand-dot"></div>
    <p class="brand-name">Harbor Ridge<br>Exteriors</p>
    <p class="tagline">ROOFING • GUTTERS • WINDOWS</p>
  </section>

  <section class="lawn-sign lawn-sign--blue">
    <svg class="lawn-sign__art" viewBox="0 0 440 301" width="440" height="301" aria-hidden="true">
      <defs>
        <linearGradient id="accent-green-b" x1="0" x2="1" y1="0" y2="0">
          <stop offset="0" stop-color="#1f9345"/>
          <stop offset="1" stop-color="#8cc63f"/>
        </linearGradient>
        <linearGradient id="band-blue" x1="0" x2="1" y1="0" y2="0">
          <stop offset="0" stop-color="#2a8ccb"/>
          <stop offset="1" stop-color="#1b2f5e"/>
        </linearGradient>
      </defs>
      <path d="M0 166 Q220 236 440 164 L440 301 L0 301 Z" fill="url(#accent-green-b)"/>
      <path d="M0 182 Q220 226 440 176 L440 301 L0 301 Z" fill="url(#band-blue)"/>
    </svg>
    <div class="brand-dot"></div>
    <p class="brand-name">Harbor Ridge<br>Exteriors</p>
    <p class="tagline">ROOFING • GUTTERS • WINDOWS</p>
  </section>

</body>
</html>
```